Music Industry Business Needs a Business Card Design

Copper Lantern is an audio mastering company that has been in business for 20 years. Mastering is the final creative step in the music production chain. Our job is to make the music sound as good as it possibly can prior to release to the public. Our world is technical, artistic, precise. We work on everything from independent artists to the music for the Grandfield Cup. We are looking for a new, more modern business card design. I am uploading a copy of our logo, although it doesn't absolutely need to be included in the design.

Target Market(s)

Music Industry Professionals

Industry/Entity Type

Business

Contact Information for Business Card

Address, Phone, Email, Website, Name, Job Title

Font styles to use
Sans Serif

Requirements
Must have
• Sorry, but I don't have any concrete things to request. If I had a clear idea of what I want, I would probably just design something myself. I am looking for fresh input and thought I would try this.
Should not have
• Anything that is typical, such as headphones or the like.

```html
<!DOCTYPE html>
<html lang="en">
<head>
<meta charset="utf-8">
<title>Copper Lantern – Business Card</title>
<link href="https://fonts.googleapis.com/css2?family=Inter:wght@700;800&display=swap" rel="stylesheet">
<style>
  :root {
    --backdrop: #1c1c1d;
    --card-black: #050505;
    --text-white: #ecece9;
    --url-green: #4fb83a;
    --spectrum-magenta: #e0167a;
    --spectrum-violet: #8a1fd6;
    --spectrum-blue: #2a3ee8;
    --spectrum-cyan: #19b5c9;
    --spectrum-green: #22c84a;
  }
  html, body {
    margin: 0;
    padding: 0;
    width: 1200px;
    height: 758px;
    overflow: hidden;
    background: var(--backdrop);
  }
  .stage {
    position: relative;
    width: 1200px;
    height: 758px;
    display: flex;
    align-items: center;
    justify-content: center;
  }
  .card {
    position: relative;
    width: 900px;
    height: 514px;
    background: var(--card-black);
    overflow: hidden;
    font-family: "Inter", "Helvetica Neue", Arial, sans-serif;
  }
  .spectrum-light {
    position: absolute;
    inset: 0;
    background:
      linear-gradient(to bottom, rgba(5,5,5,0) 0%, rgba(5,5,5,0.35) 45%, rgba(5,5,5,0.92) 85%, var(--card-black) 100%),
      linear-gradient(to right,
        rgba(5,5,5,1) 0%,
        var(--spectrum-magenta) 14%,
        var(--spectrum-violet) 30%,
        var(--spectrum-blue) 50%,
        var(--spectrum-cyan) 68%,
        var(--spectrum-green) 86%,
        rgba(5,5,5,1) 100%);
    opacity: 0.85;
  }
  .tagline {
    position: absolute;
    left: 108px;
    top: 232px;
    margin: 0;
    color: var(--text-white);
    font-weight: 700;
    font-size: 37px;
    line-height: 33px;
    letter-spacing: -0.3px;
  }
  .web-address {
    position: absolute;
    left: 108px;
    top: 420px;
    margin: 0;
    color: var(--url-green);
    font-weight: 700;
    font-size: 37px;
    letter-spacing: -0.3px;
  }
</style>
</head>
<body>
  <main class="stage">
    <section class="card" aria-label="Copper Lantern business card">
      <div class="spectrum-light" role="img" aria-label="Streaks of spectrum light from magenta through blue to green falling down the card"></div>
      <p class="tagline">your music is the most<br>important thing you do<br>mastering your music<br>is the most important<br>thing we do</p>
      <p class="web-address">www.copperlantern.ca/contact</p>
    </section>
  </main>
</body>
</html>
```